Quarlen - Business Card Design

Design a modern masculine business card for our business

Target Market(s)

Private Market

Industry/Entity Type

Construction

Contact Information for Business Card

Company Name - Name of Person - Address - email address - contact number

Font styles to use
Serif
Sans Serif

Colors
0094D4
00A9DD
6FCCEA
C7EBF8
E9F6FB
00AB8E
00BBA5
67D7C9
C6EFE9
E9F9F6
F0912C
F2A743
F7CA91
FBE8D2
FDF5EE

Requirements
Must have
• Use company logo provided
Nice to have
• Company Logo

```html
<!DOCTYPE html>
<html lang="en">
<head>
<meta charset="utf-8">
<title>Quarlen Construction – Business Card</title>
<link href="https://fonts.googleapis.com/css2?family=Montserrat:wght@400;500;700;800&display=swap" rel="stylesheet">
<style>
  :root {
    --bg: #3a3a3a;
    --ink: #0a0a0a;
    --paper: #ffffff;
    --accent: #f47a20;
    --rule: #666666;
  }
  html, body {
    margin: 0;
    width: 1200px;
    height: 1200px;
    overflow: hidden;
    background: var(--bg);
    font-family: "Montserrat", sans-serif;
  }
  .card {
    position: absolute;
    left: 200px;
    width: 800px;
    height: 457px;
    border-radius: 28px;
    overflow: hidden;
    box-shadow: 0 14px 30px rgba(0,0,0,0.45);
  }
  .card--front { top: 90px; background: var(--paper); }
  .card--back { top: 650px; background: var(--ink); }
  .card__bands { position: absolute; inset: 0; }
  .brand {
    position: absolute;
    left: 0;
    right: 0;
    display: flex;
    align-items: center;
    justify-content: center;
    gap: 16px;
    font-weight: 800;
    letter-spacing: 1px;
    white-space: nowrap;
  }
  .brand__mark { width: 28px; height: 28px; background: var(--accent); }
  .brand__name { font-size: 38px; line-height: 1; }
  .card--front .brand { top: 110px; color: var(--ink); }
  .card--back .brand { top: 210px; color: var(--paper); }
  .holder {
    position: absolute;
    left: 64px;
    top: 355px;
    padding-left: 18px;
    border-left: 5px solid var(--accent);
  }
  .holder__name {
    color: var(--accent);
    font-weight: 500;
    font-size: 34px;
    line-height: 1;
    letter-spacing: 0.5px;
  }
  .holder__role {
    color: var(--paper);
    font-size: 18px;
    margin-top: 6px;
    letter-spacing: 0.5px;
  }
  .divider {
    position: absolute;
    left: 400px;
    top: 300px;
    width: 1px;
    height: 115px;
    background: var(--rule);
  }
  .contact {
    position: absolute;
    left: 440px;
    top: 290px;
    margin: 0;
    padding: 0;
    list-style: none;
    color: var(--paper);
    font-size: 18px;
    line-height: 1.3;
  }
  .contact li { display: flex; align-items: flex-start; gap: 10px; margin-bottom: 6px; }
  .contact svg { flex: none; width: 18px; height: 18px; margin-top: 3px; fill: var(--accent); }
</style>
</head>
<body>

<section class="card card--front">
  <svg class="card__bands" viewBox="0 0 800 457" preserveAspectRatio="none" aria-hidden="true">
    <polygon points="0,300 800,215 800,457 0,457" fill="#0a0a0a"/>
    <polygon points="0,289 800,204 800,213 0,298" fill="#f47a20"/>
  </svg>

  <div class="brand">
    <span class="brand__mark"></span>
    <span class="brand__name">QUARLEN CONSTRUCTION, INC</span>
  </div>

  <div class="holder">
    <div class="holder__name">FULL NAME</div>
    <div class="holder__role">POSITION</div>
  </div>

  <div class="divider"></div>

  <ul class="contact">
    <li>
      <svg viewBox="0 0 24 24"><path d="M6.6 10.8a15.1 15.1 0 0 0 6.6 6.6l2.2-2.2a1 1 0 0 1 1-.25 11.4 11.4 0 0 0 3.6.57 1 1 0 0 1 1 1V20a1 1 0 0 1-1 1A17 17 0 0 1 3 4a1 1 0 0 1 1-1h3.5a1 1 0 0 1 1 1c0 1.25.2 2.45.57 3.57a1 1 0 0 1-.25 1z"/></svg>
      <span>(000) 000 0000</span>
    </li>
    <li>
      <svg viewBox="0 0 24 24"><path d="M2 5h20v14H2zm2 2v.5l8 5 8-5V7l-8 5z"/></svg>
      <span>email@company.com</span>
    </li>
    <li>
      <svg viewBox="0 0 24 24"><path d="M12 2a7 7 0 0 0-7 7c0 5.2 7 13 7 13s7-7.8 7-13a7 7 0 0 0-7-7zm0 9.5A2.5 2.5 0 1 1 12 6.5a2.5 2.5 0 0 1 0 5z"/></svg>
      <span>123 Name Street, 000<br>Your City, 00000-000</span>
    </li>
  </ul>
</section>

<section class="card card--back">
  <div class="brand">
    <span class="brand__mark"></span>
    <span class="brand__name">QUARLEN CONSTRUCTION, INC</span>
  </div>
</section>

</body>
</html>
```